Fish Farm needing 3 - Fold Flyer / Price List designed

We are looking for a new Price List for our Fish Farm. I have attached an example of the basic info that needs in the flyer. We want the flyer to be a 3 fold page. Anything that is on our website, you can use for ideas. There are some pictures on there that can be photoshopped into the flyer. Do not use any photos from any other sites. We are looking for something professional but fun and exciting! I have also attached our business logo. We tend to stay with the blues and greens for colors. Let's get started....
Updates

Need extra days to review

Contact Information for Business Card

We are needing a business card with our new logo on it. We also need our address, phone numbers, email address, and website listed. Please view our website for more ideas.

Colors

Designer to choose colors to be used in the design.

```html
<!DOCTYPE html>
<html lang="en">
<head>
<meta charset="utf-8">
<title>Brookhollow Fish Farm – Tri-fold Price List</title>
<link rel="stylesheet" href="https://fonts.googleapis.com/css2?family=Oswald:wght@500;600&family=Open+Sans:wght@400;600;700&display=swap">
<style>
:root{
  --blue:#1f74c1;
  --navy:#23338f;
  --slate:#5d6064;
  --ink:#222;
  --row-grey:#c4c4c4;
  --paper:#fff;
  --backdrop:#dcdcdc;
  --map-tone:#eef0f2;
}
*{box-sizing:border-box;margin:0;padding:0}
html,body{width:933px;height:1200px;overflow:hidden;background:var(--backdrop)}
body{font-family:"Open Sans",sans-serif;color:var(--ink)}
.canvas{position:relative;width:933px;height:1200px}
.spread{position:absolute;left:106px;width:720px;height:556px;background:var(--paper);display:flex;box-shadow:0 4px 14px rgba(0,0,0,.18)}
.spread--outside{top:30px}
.spread--inside{top:614px}
.panel{position:relative;width:240px;height:556px;overflow:hidden}
.panel+.panel{border-left:1px solid #ececec}
.heading{font-family:"Oswald",sans-serif;font-weight:600;text-transform:uppercase;letter-spacing:.3px}
.brand{font-family:"Open Sans",sans-serif;font-weight:700;color:var(--navy);font-size:15px;text-align:center;display:flex;align-items:center;justify-content:center;gap:6px}
.brand-dot{width:9px;height:9px;border-radius:50%;background:var(--blue)}

/* outside – left panel */
.map{position:absolute;left:16px;top:14px;width:208px;height:150px;background:var(--map-tone)}
.price-band{position:absolute;left:0;top:176px;width:240px;height:150px;background:var(--slate);color:#fff;padding:14px 16px}
.price-band .heading{font-size:22px;line-height:1.1;margin-bottom:8px}
.price-band .cols{display:flex;gap:14px;font-size:10px;line-height:1.35;font-style:italic}
.call-text{position:absolute;left:16px;top:340px;width:210px;font-size:9.5px;line-height:1.45}
.call-text p{margin-bottom:8px}
.pill{display:inline-block;border-radius:14px;padding:5px 12px;font-size:9.5px;white-space:nowrap}
.pill--blue{background:var(--blue);color:#fff}
.pill--white{background:#fff;color:var(--ink)}
.left-pill{position:absolute;left:16px;top:500px}

/* outside – middle panel */
.wave{position:absolute;inset:0}
.mid-brand{position:absolute;top:24px;left:0;width:100%}
.stocking{position:absolute;top:62px;width:100%;text-align:center}
.stocking .heading{color:var(--navy);font-size:21px;line-height:1.05}
.stocking h3{font-size:11px;font-weight:700;margin:8px 0 6px}
.stocking ul{list-style:none;font-size:9px;line-height:1.45}
.contacts{position:absolute;left:24px;top:370px;color:#fff;font-size:11px;line-height:1.55}
.contacts b{font-weight:700}
.mid-pill{position:absolute;left:22px;top:490px}

/* outside – right panel */
.right-brand{position:absolute;top:24px;left:0;width:100%}
.photo{position:absolute;inset:0}
.company{position:absolute;left:22px;top:362px;color:#fff}
.company .heading{font-size:22px;line-height:1.1}
.company p{font-size:9.5px;line-height:1.4;margin-top:4px}
.right-pill{position:absolute;left:22px;top:470px}

/* inside price tables */
.inner{padding:12px 14px 0}
.price{width:100%;border-collapse:collapse;margin-bottom:9px;font-size:9.5px}
.price caption{background:var(--blue);color:#fff;padding:3px 4px;font-family:"Oswald",sans-serif;font-weight:600;font-size:12px;text-transform:uppercase;line-height:1.1}
.price caption small{display:block;font-family:"Open Sans",sans-serif;font-weight:400;font-size:7.5px;text-transform:none}
.price th,.price td{border:1px solid #555;padding:1.5px 5px;text-align:left;height:15px}
.price th{font-weight:600;font-size:10px}
.price tbody tr:nth-child(odd) td{background:var(--row-grey)}
.price .note-row td{text-align:center;background:#fff !important}
.footnote{font-size:9px;font-weight:700;font-style:italic;margin-top:4px}
.disclaimer{font-size:12px;font-weight:600;margin-top:6px;line-height:1.3}
.small-note{font-size:8.5px;font-style:italic;margin-top:2px}
</style>
</head>
<body>
<div class="canvas">

  <!-- Outside of the tri-fold -->
  <section class="spread spread--outside">
    <div class="panel panel--directions">
      <div class="map" role="img" aria-label="Road map showing the route from the highway exit to the farm"></div>
      <div class="price-band">
        <h2 class="heading">2019 Price List For:</h2>
        <div class="cols">
          <div>Hybrid bluegill<br>Regular bluegill<br>Redear sunfish<br>Largemouth bass<br>Fathead minnows<br>Golden shiners<br>Triploid grass carp</div>
          <div>Channel catfish<br>Albino catfish<br>Black crappie<br>Japanese koi<br>Tilapia<br>Fish food</div>
        </div>
      </div>
      <div class="call-text">
        <p>Feel free to call the farm or the cell phone. If no answer, leave a message and we will get back to you as soon as possible.</p>
        <p>Always call before coming to the farm as we may be on a delivery.</p>
        <p>Our Sales Route Schedule is listed on our website at:</p>
      </div>
      <span class="pill pill--blue left-pill">www.brookhollowfishfarm.com/schedule</span>
    </div>

    <div class="panel panel--contact">
      <svg class="wave" width="240" height="556" viewBox="0 0 240 556" aria-hidden="true">
        <path d="M0 300 Q110 360 240 250 L240 556 L0 556 Z" fill="var(--blue)"/>
      </svg>
      <div class="brand mid-brand"><span class="brand-dot"></span>Brookhollow Fish Farm</div>
      <div class="stocking">
        <h2 class="heading">Standard<br>Stocking Rates</h2>
        <h3>Per Surface Acre</h3>
        <ul>
          <li>600-1,000 Hybrid Bluegill,</li>
          <li>Regular Bluegill, or Redear</li>
          <li>100-200 Largemouth Bass</li>
          <li>100-200 Channel Catfish</li>
          <li>3,000-5,000 Fathead Minnows</li>
        </ul>
      </div>
      <div class="contacts">
        <div><b>Farm:</b> (555) 201-4410</div>
        <div><b>Cell:</b> (555) 201-4432</div>
        <div><b>Text:</b> (555) 201-4400</div>
        <div>brookhollowfish@mailpond.net</div>
      </div>
      <span class="pill pill--white mid-pill">www.brookhollowfishfarm.com</span>
    </div>

    <div class="panel panel--cover">
      <svg class="photo" width="240" height="556" viewBox="0 0 240 556">
        <defs>
          <linearGradient id="sea" x1="0" y1="0" x2="0" y2="1">
            <stop offset="0" stop-color="#c9b8c8"/>
            <stop offset=".55" stop-color="#8aa6bf"/>
            <stop offset="1" stop-color="#2f6f9c"/>
          </linearGradient>
        </defs>
        <path d="M0 250 Q130 330 240 200 L240 556 L0 556 Z" fill="var(--blue)"/>
        <path d="M40 78 Q140 52 240 58" fill="none" stroke="var(--navy)" stroke-width="4"/>
        <path role="img" aria-label="Photo of fishing nets over calm water at dusk" d="M32 86 Q140 62 240 68 L240 220 Q140 300 50 260 Q20 180 32 86 Z" fill="url(#sea)"/>
      </svg>
      <div class="brand right-brand"><span class="brand-dot"></span>Brookhollow Fish Farm</div>
      <div class="company">
        <h1 class="heading">Brookhollow<br>Fish Farm, LLC</h1>
        <p>4870 N. Heron Pond Rd.<br>Millbrook, IN 47000</p>
      </div>
      <span class="pill pill--white right-pill">www.brookhollowfishfarm.com</span>
    </div>
  </section>

  <!-- Inside of the tri-fold -->
  <section class="spread spread--inside">
    <div class="panel"><div class="inner">
      <table class="price">
        <caption>Hybrid Bluegill<br>(Hybrid Sunfish)</caption>
        <thead><tr><th>Size</th><th>Each</th><th>1000</th><th>3000</th></tr></thead>
        <tbody>
          <tr><td>1-3 Inch</td><td>50¢</td><td>45¢</td><td>40¢</td></tr>
          <tr><td>3-5 Inch</td><td>80¢</td><td>75¢</td><td></td></tr>
          <tr><td>★ 5-7 Inch</td><td>$1.75</td><td></td><td></td></tr>
        </tbody>
      </table>
      <table class="price">
        <caption>Regular Bluegill</caption>
        <thead><tr><th>Size</th><th>Each</th><th>1000</th></tr></thead>
        <tbody>
          <tr><td>1-3 Inch</td><td>50¢</td><td>45¢</td></tr>
          <tr><td>★ 3-5 Inch</td><td>80¢</td><td>75¢</td></tr>
        </tbody>
      </table>
      <table class="price">
        <caption>Redear Sunfish</caption>
        <thead><tr><th>Size</th><th>Each</th><th>1000</th></tr></thead>
        <tbody>
          <tr><td>1-3 Inch</td><td>50¢</td><td>45¢</td></tr>
          <tr><td>3-4 Inch</td><td>75¢</td><td>70¢</td></tr>
          <tr><td>★ 3-5 Inch</td><td>$1.00</td><td>95¢</td></tr>
        </tbody>
      </table>
      <table class="price">
        <caption>Redear Sunfish</caption>
        <thead><tr><th>Size</th><th>Each</th></tr></thead>
        <tbody>
          <tr><td>3 Inch</td><td>$1.10</td></tr>
          <tr><td>3-4 Inch</td><td>$1.20</td></tr>
          <tr><td>★ 4-6 Inch</td><td>$1.95</td></tr>
          <tr><td>★ 6-8 Inch</td><td>$2.75</td></tr>
        </tbody>
      </table>
      <p class="footnote">★ When Available. Sizes Vary Depending on Time of Year</p>
    </div></div>

    <div class="panel"><div class="inner">
      <table class="price">
        <caption>Triploid Grass Carp<small>(Indiana Prices)</small></caption>
        <thead><tr><th>8-11 Inch</th><th>Minimum 5</th></tr></thead>
        <tbody>
          <tr><td>5-24 Grass Carp</td><td>$16.00 each</td></tr>
          <tr><td>25-49 Grass Carp</td><td>$15.00 each</td></tr>
          <tr><td>50-99 Grass Carp</td><td>$14.00 each</td></tr>
          <tr><td>100+ Grass Carp</td><td>Inquire</td></tr>
        </tbody>
      </table>
      <table class="price">
        <caption>Channel Catfish</caption>
        <thead><tr><th>Size</th><th>Each</th><th>1000</th></tr></thead>
        <tbody><tr><td>6-8 Inch</td><td>65¢</td><td>60¢</td></tr></tbody>
      </table>
      <table class="price">
        <caption>Albino Catfish<small>(March &amp; April)</small></caption>
        <thead><tr><th>Size</th><th>Each</th></tr></thead>
        <tbody><tr><td>5-8 Inch</td><td>$1.20</td></tr></tbody>
      </table>
      <table class="price">
        <caption>Black Crappie<small>(March &amp; April)</small></caption>
        <thead><tr><th>Size</th><th>Each</th></tr></thead>
        <tbody><tr><td>3-5 Inch</td><td>$1.10</td></tr></tbody>
      </table>
      <table class="price">
        <caption>Fathead Minnows</caption>
        <tbody><tr class="note-row"><td>$36.00 per thousand<br>($9.00 per lb.)</td></tr></tbody>
      </table>
    </div></div>

    <div class="panel"><div class="inner">
      <table class="price">
        <caption>Golden Shiners<small>(Delivery Only - Minimum 50 lb.)</small></caption>
        <tbody>
          <tr><td>50-99 lb.</td><td>$8.00 lb.</td></tr>
          <tr><td>100+ lb.</td><td>$7.50 lb.</td></tr>
        </tbody>
      </table>
      <table class="price">
        <caption>Floating Fish Food</caption>
        <tbody><tr class="note-row"><td>Starter Size (50 lb. Bag)<br>41% Protein<br>Market Price - Inquire<br>(Only Available at Farm)</td></tr></tbody>
      </table>
      <table class="price">
        <caption>Tilapia<small>(May 15 - June 30)</small></caption>
        <thead><tr><th colspan="2">5-10 Tilapia per lb.</th></tr></thead>
        <tbody>
          <tr><td>1-25 lb.</td><td>$15.00 each</td></tr>
          <tr><td>26-40 lb.</td><td>$14.00 each</td></tr>
          <tr><td>40-50 lb.</td><td>$13.00 each</td></tr>
          <tr><td>50+ lb.</td><td>$12.00 each</td></tr>
        </tbody>
      </table>
      <table class="price">
        <caption>Japanese Koi</caption>
        <thead><tr><th>Size</th><th>Each</th></tr></thead>
        <tbody>
          <tr><td>4-5 Inch</td><td>$6.00</td></tr>
          <tr><td>6-8 Inch</td><td>$10.00</td></tr>
          <tr><td>★ 9-12 Inch</td><td>$15.00</td></tr>
        </tbody>
      </table>
      <p class="small-note">Butterfly koi Also available!</p>
      <p class="disclaimer">Prices subject to change without notice</p>
    </div></div>
  </section>

</div>
</body>
</html>
```